Harbor Business Cards

I need a business card designed with the following information.

Company Name: Harbor Wealth Management
Name: BriAnne Dockery
Title: Executive Assistant
Cell: (281) 555-0173
Direct Line: (832) 555-0148
Email: brianne@harborwmx.com
Address: 20537 W. Marlowe PKWY Ste. B
Brenwick, TX 77390

I have attached the logo.
I would like it in navy blue and silver.
Thanks.

```html
<!DOCTYPE html>
<html lang="en">
<head>
<meta charset="utf-8">
<title>Harbor Wealth Management – Business Card</title>
<link href="https://fonts.googleapis.com/css2?family=Lato:wght@300;400;700&display=swap" rel="stylesheet">
<style>
  :root {
    --backdrop: #b3b3b3;
    --navy: #0f2344;
    --silver: #b5b5b5;
    --silver-light: #e4e4e4;
    --white: #f2f2f2;
    --divider: #3a4b68;
  }
  html, body {
    margin: 0;
    padding: 0;
    width: 1200px;
    height: 900px;
    overflow: hidden;
    background: var(--backdrop);
    font-family: "Lato", sans-serif;
  }
  .canvas {
    position: relative;
    width: 1200px;
    height: 900px;
  }
  .card {
    position: absolute;
    top: 275px;
    width: 478px;
    height: 295px;
    background: var(--navy);
    overflow: hidden;
  }
  .card--front {
    left: 120px;
    border-radius: 0 46px 0 46px;
  }
  .card--back {
    left: 620px;
    border-radius: 46px 0 46px 0;
  }
  .brand-mark {
    position: absolute;
    left: 66px;
    top: 118px;
    width: 150px;
    display: flex;
    align-items: center;
    gap: 8px;
    color: var(--silver-light);
    font-weight: 300;
    font-size: 26px;
    letter-spacing: 5px;
  }
  .brand-mark__square {
    width: 14px;
    height: 14px;
    background: var(--silver-light);
    flex: none;
  }
  .divider {
    position: absolute;
    left: 239px;
    top: 75px;
    width: 1px;
    height: 138px;
    background: var(--divider);
  }
  .details {
    position: absolute;
    left: 272px;
    top: 76px;
    color: var(--white);
  }
  .details__name {
    margin: 0;
    font-size: 18px;
    font-weight: 700;
    letter-spacing: 0.5px;
    color: var(--silver);
    text-transform: uppercase;
    line-height: 22px;
  }
  .details__title {
    margin: 0 0 6px;
    font-size: 13px;
    line-height: 16px;
  }
  .contact {
    list-style: none;
    margin: 0;
    padding: 0;
    font-size: 13.5px;
    line-height: 17.5px;
  }
  .contact li {
    display: flex;
    align-items: center;
    gap: 4px;
  }
  .contact svg {
    width: 10px;
    height: 10px;
    fill: var(--silver);
    flex: none;
  }
  .contact__note { font-size: 12px; }
  .details__address {
    margin: 5px 0 0;
    font-size: 13.5px;
    line-height: 17px;
    font-style: normal;
  }
  .wordmark {
    position: absolute;
    left: 0;
    right: 0;
    top: 178px;
    text-align: center;
    color: var(--silver-light);
    font-weight: 300;
  }
  .wordmark__name {
    display: block;
    font-size: 27px;
    letter-spacing: 9px;
    padding-left: 9px;
  }
  .wordmark__sub {
    display: block;
    margin-top: 6px;
    font-size: 10.5px;
    letter-spacing: 3px;
    padding-left: 3px;
  }
</style>
</head>
<body>
<main class="canvas">
  <section class="card card--front" aria-label="Business card front">
    <div class="brand-mark">
      <span class="brand-mark__square"></span>
      <span>HARBOR</span>
    </div>
    <div class="divider"></div>
    <div class="details">
      <h1 class="details__name">BriAnne Dockery</h1>
      <p class="details__title">Executive Assistant</p>
      <ul class="contact">
        <li>
          <svg viewBox="0 0 10 10" aria-hidden="true"><path d="M2.5 0h5a1 1 0 0 1 1 1v8a1 1 0 0 1-1 1h-5a1 1 0 0 1-1-1V1a1 1 0 0 1 1-1zm.6 1.2v6.6h3.8V1.2z"/></svg>
          <span>(281) 555-0173</span>
        </li>
        <li>
          <svg viewBox="0 0 10 10" aria-hidden="true"><path d="M0 3.5C2.5.8 7.5.8 10 3.5L8.6 4.8 7 3.8V2.9C5.7 2.4 4.3 2.4 3 2.9v.9L1.4 4.8zM2 5.5h6L9 9.5H1z"/></svg>
          <span>(832) 555-0148<span class="contact__note">(DIRECT)</span></span>
        </li>
        <li>
          <svg viewBox="0 0 10 10" aria-hidden="true"><path d="M0 2h10v6H0zm.8.8v.3L5 5.6l4.2-2.5v-.3z"/></svg>
          <span>brianne@harborwmx.com</span>
        </li>
      </ul>
      <address class="details__address">20537 W. Marlowe PKWY<br>Ste. B, Brenwick, TX 77390</address>
    </div>
  </section>

  <section class="card card--back" aria-label="Business card back">
    <div class="wordmark">
      <span class="wordmark__name">HARBOR</span>
      <span class="wordmark__sub">WEALTH MANAGEMENT</span>
    </div>
  </section>
</main>
</body>
</html>
```